New, High-Tech Website for Venture Z - A Product Development Company

Venture Z is located in Silicon Valley, CA. We help companies build products from start to finish and everywhere in between. We build teams with top talent based on our customer's needs. We need a BRAND NEW website that looks innovative, fresh, new & modern. We want our website to impress companies that will hire us, as well as developers, designers, product people, etc.

The design is very important!

Target Market(s)

Small companies, entrepreneurs, anyone who needs help building a product or finding top talent

Industry/Entity Type

Tech

Coding

Coded - Design and coding required

Font styles to use
Sans Serif

Requirements
Must have
• Our logo (attached) and colors that look good with the logo.

**UPDATE - Site should be fully coded for WordPress and be MOBILE FRIENDLY. (Responsive Designs)
Nice to have
• We would love to see your ideas and if you have any other cool ideas to make our site POP and look attractive.

Please also let us know the following when you submit your design (in the notes section)!

1) Are we able to use any illustrations or images you provided legally? Would we need to pay any additional fees for images or illustrations?  If so, how much per picture/illustration?

2) If we choose your design, do your services include deploying the design to our Wordpress site?  Or, do you charge extra for this and how much?

3) If we choose your design, will this include any other page designs?  If so, how many?

4) If we choose your design, how much will you charge to design and implement other pages for us (like our contact us page, careers page, site map page, etc.) so our website looks cohesive?

5) What is your turnaround time for further page designs and implementations to the site?

6) Can you design AND implement surveys and/or custom questionnaires? What is the cost?
Should not have
• Nothing too "corporate" looking. For example, no images with men in suits around a large conference room because this doesn't represent who we are. We are more looking for images of people working - small startup company style.

Really cool, high tech illustrations are good too.

```html
<!DOCTYPE html>
<html lang="en">
<head>
<meta charset="utf-8">
<title>Venture Z — Product Development</title>
<link href="https://fonts.googleapis.com/css2?family=Montserrat:wght@400;500;600;700&display=swap" rel="stylesheet">
<style>
:root{
  --teal:#2bbfb2;
  --cyan:#27c3e6;
  --ink:#2c3748;
  --body:#5a6270;
  --mute:#8a909b;
  --navy:#2b3b58;
  --navy-2:#33435f;
  --soft:#f1f3f6;
  --white:#ffffff;
}
*{box-sizing:border-box;margin:0;padding:0}
html,body{width:1200px;height:4508px;overflow:hidden}
body{position:relative;background:var(--white);font-family:"Montserrat",sans-serif;color:var(--ink)}
.abs{position:absolute}
a{color:inherit;text-decoration:none}

/* header */
.site-header{position:absolute;left:0;top:0;width:1200px;height:120px;background:var(--white)}
.brand{position:absolute;left:44px;top:40px;display:flex;align-items:center;gap:10px;font-weight:700;font-size:22px;color:var(--teal)}
.brand-dot{width:26px;height:26px;border-radius:50%;background:var(--teal)}
.nav a{position:absolute;top:50px;font-size:13.5px;font-weight:500;color:var(--ink)}
.nav a.active{color:var(--teal)}
.pill{position:absolute;height:36px;border-radius:18px;background:var(--teal);color:#fff;font-size:12px;font-weight:600;display:flex;align-items:center;justify-content:center}

/* hero */
.hero-media{position:absolute;left:0;top:120px;width:1200px;height:660px;background:linear-gradient(120deg,#8e9aa6 0%,#6f8096 40%,#5d6f88 70%,#a9b5c2 100%)}
.hero-title{position:absolute;left:88px;top:300px;font-size:50px;font-weight:500;color:#fff}
.hero-sub{position:absolute;left:88px;top:372px;font-size:24px;line-height:30px;color:#fff;font-weight:400}
.hero-sub b{font-weight:600}

/* intro */
.intro{position:absolute;left:0;top:760px;width:1200px;height:320px;background:#fff;box-shadow:0 14px 20px -12px rgba(0,0,0,.12);text-align:center}
.h-main{font-size:38px;font-weight:400;color:var(--ink)}
.h-accent{font-size:38px;font-weight:400;color:var(--teal)}
.intro p{font-size:12.5px;line-height:19px;color:var(--body);width:800px;margin:0 auto}
.btn-outline{position:absolute;height:36px;border:2px solid var(--teal);border-radius:18px;font-size:12px;font-weight:600;color:var(--ink);display:flex;align-items:center;justify-content:center;background:#fff}

/* feature rows */
.photo{position:absolute;width:376px;height:455px;border-radius:0 50px 50px 0}
.accent-block{position:absolute;width:184px;height:262px;background:linear-gradient(160deg,var(--teal),#24b7c9)}
.feature h2{font-size:32px;font-weight:500;color:var(--ink)}
.ticks{list-style:none}
.ticks li{position:relative;padding-left:28px;font-size:13.5px;line-height:19px;color:var(--body)}
.ticks li::before{content:"";position:absolute;left:0;top:3px;width:11px;height:11px;border:1.5px solid var(--teal);border-radius:50%}
.ticks li::after{content:"";position:absolute;left:4px;top:6px;width:3px;height:5px;border:solid var(--teal);border-width:0 1.5px 1.5px 0;transform:rotate(45deg)}

/* process */
.process{position:absolute;left:0;top:2770px;width:1200px;height:640px;background:var(--soft)}
.step-label{position:absolute;text-align:center;font-size:15px;font-weight:600;line-height:19px;color:var(--ink);width:180px}
.step-art{position:absolute;width:150px;height:100px;border-radius:8px}

/* services */
.services-title{position:absolute;left:0;width:1200px;text-align:center}
.card{position:absolute;top:3553px;width:256px;height:302px;text-align:center}
.card.featured{background:linear-gradient(160deg,var(--cyan),var(--teal))}
.card .icon{width:50px;height:50px;margin:44px auto 0;border:2.5px solid var(--teal);border-radius:10px}
.card.featured .icon{border-color:#fff}
.card h3{margin-top:30px;font-size:18px;font-weight:500;color:var(--ink)}
.card p{margin:10px auto 0;width:220px;font-size:11.5px;line-height:19px;color:var(--mute)}
.card.featured h3,.card.featured p{color:#fff}
.card .btn-outline{left:64px;top:250px;width:128px;height:34px}
.card.featured .btn-outline{border-color:#fff;color:var(--teal)}
.col-divider{position:absolute;left:856px;top:3553px;width:1px;height:302px;background:#e2e5ea}

/* footer */
.footer{position:absolute;left:0;top:3975px;width:1200px;height:533px;background:linear-gradient(180deg,var(--navy-2),var(--navy))}
.f-brand{position:absolute;left:88px;top:4170px;display:flex;align-items:center;gap:10px;font-weight:700;font-size:22px;color:#fff}
.f-brand .brand-dot{background:var(--teal)}
.f-call{position:absolute;left:88px;top:4253px;font-size:24px;color:#fff;font-weight:400}
.f-mail{position:absolute;left:88px;top:4287px;font-size:13px;color:#d3d9e3}
.social{position:absolute;top:4335px;width:38px;height:38px;border-radius:50%;background:#fff}
.social.active{background:var(--teal)}
.f-head{position:absolute;font-size:20px;font-weight:500;color:#fff}
.quick{position:absolute;left:506px;top:4226px;list-style:none}
.quick li{font-size:12px;line-height:24px;color:#c9d0dc}
.subscribe{position:absolute;left:793px;top:4153px;width:320px;height:240px;background:linear-gradient(160deg,var(--cyan),var(--teal))}
.field{position:absolute;left:22px;width:276px;height:34px;border-radius:17px;background:#fff;font-size:11px;color:var(--mute);padding-left:16px;display:flex;align-items:center}
.submit{position:absolute;left:22px;top:192px;width:112px;height:34px;border-radius:17px;background:#fff;color:var(--teal);font-size:12px;font-weight:600;display:flex;align-items:center;justify-content:center}
.legal{position:absolute;top:4442px;font-size:12px;color:#c9d0dc}
.legal .hl{color:var(--teal)}
</style>
</head>
<body>

<header class="site-header">
  <div class="brand"><span class="brand-dot"></span>Venture Z</div>
  <nav class="nav">
    <a class="active" style="left:238px">Home</a>
    <a style="left:310px">Services</a>
    <a style="left:400px">About</a>
    <a style="left:474px">Testimonials &amp; Press</a>
    <a style="left:646px">Careers</a>
    <a style="left:731px">Blog</a>
  </nav>
  <a class="pill" style="left:796px;top:42px;width:177px">Freelancers - Apply Now</a>
  <a class="pill" style="left:980px;top:42px;width:177px">Companies - Get in Touch</a>
</header>

<section>
  <div class="hero-media" role="img" aria-label="Hands typing on a laptop with glowing technology icons overlaid"></div>
  <h1 class="hero-title">Welcome to Venture Z</h1>
  <p class="hero-sub">The #1 leader in <b>product development services,</b><br>based in Silicon Valley, CA</p>
  <a class="pill" style="left:88px;top:460px;width:126px;height:34px">Contact Us</a>
  <svg class="abs" style="left:0;top:600px" width="1200" height="180" viewBox="0 600 1200 180">
    <path d="M0 761 Q600 621 1200 761 L1200 780 L0 780 Z" fill="#fff"/>
    <path d="M250 712 Q600 640 950 712" fill="none" stroke="#2bbfb2" stroke-width="5"/>
    <circle cx="600" cy="683" r="40" fill="#2bbfb2" stroke="#fff" stroke-width="5"/>
  </svg>
</section>

<section class="intro">
  <h2 class="h-main" style="margin-top:40px">Need help building a product?</h2>
  <h2 class="h-accent" style="margin-top:2px">We are here for you!</h2>
  <p style="margin-top:14px">Venture Z works with companies of all sizes to design, build &amp; launch exceptional products from start to finish<br>(and anywhere in between.)&nbsp; We take ideas from concept to launch, or can step into organizations that are experiencing<br>product troubles and advise on how to clear roadblocks.</p>
  <a class="btn-outline" style="left:512px;top:228px;width:176px">Explore Our Services</a>
</section>

<!-- We love to work with -->
<section class="feature">
  <div class="accent-block" style="left:88px;top:1400px"></div>
  <div class="photo" style="left:112px;top:1185px;background:linear-gradient(135deg,#c9d4e0,#5a7391 60%,#2f4766)" role="img" aria-label="Person in a suit touching a tablet with floating interface graphics"></div>
  <h2 class="abs" style="left:616px;top:1220px">We love to work with</h2>
  <ul class="ticks abs" style="left:616px;top:1276px;width:480px">
    <li style="margin-bottom:20px">Entrepreneurs with an idea who wants to build a beta product<br>or business</li>
    <li style="margin-bottom:20px">Start Up Companies who need a product built quickly and cost<br>effectively</li>
    <li style="margin-bottom:20px">Small or medium sized, more established companies that are<br>having issues shipping product</li>
    <li style="margin-bottom:20px">Larger sized companies that need Product Management<br>consulting</li>
    <li>Companies of all sizes that need great talent, quickly.</li>
  </ul>
  <a class="btn-outline" style="left:616px;top:1561px;width:128px">Contact Us</a>
</section>

<!-- Things that excite us -->
<section class="feature">
  <h2 class="abs" style="left:88px;top:1740px">Things that excite us</h2>
  <ul class="ticks abs" style="left:88px;top:1795px;width:380px">
    <li style="margin-bottom:19.5px">Innovation</li>
    <li style="margin-bottom:19.5px">New design &amp; technology</li>
    <li style="margin-bottom:19.5px">Clear Roadmaps</li>
    <li style="margin-bottom:19.5px">Product Releases</li>
    <li style="margin-bottom:19.5px">Brining ideas to life</li>
    <li style="margin-bottom:19.5px">Solving Busines Challenges</li>
    <li>Happy Clients</li>
  </ul>
  <a class="btn-outline" style="left:88px;top:2080px;width:128px">Contact Us</a>
  <div class="accent-block" style="left:712px;top:1922px"></div>
  <div class="photo" style="left:737px;top:1706px;background:linear-gradient(135deg,#5b5048,#d8d6cf 45%,#e9e27a 55%,#6a5e54)" role="img" aria-label="Hands assembling paper pieces showing a yellow light bulb on a wooden table"></div>
</section>

<!-- Things that we promise -->
<section class="feature">
  <div class="accent-block" style="left:88px;top:2442px"></div>
  <div class="photo" style="left:112px;top:2224px;background:linear-gradient(135deg,#a8b0b8,#6d747e 50%,#d9a58c)" role="img" aria-label="Person wearing a virtual reality headset with colourful bokeh lights"></div>
  <h2 class="abs" style="left:616px;top:2280px">Things that we promise</h2>
  <ul class="ticks abs" style="left:616px;top:2336px;width:480px">
    <li style="margin-bottom:19.5px">Experience, Passion &amp; Impact</li>
    <li style="margin-bottom:19.5px">Focused strategies</li>
    <li style="margin-bottom:19.5px">Great People &amp; High Functioning Teams</li>
    <li style="margin-bottom:19.5px">Integrity, Reliability &amp; Security</li>
    <li style="margin-bottom:19.5px">Data driven &amp; Design centric results</li>
    <li>Top customer service for our clients</li>
  </ul>
  <a class="btn-outline" style="left:616px;top:2581px;width:128px">Contact Us</a>
</section>

<!-- Process -->
<section class="process"></section>
<svg class="abs" style="left:0;top:2770px" width="1200" height="640" viewBox="0 2770 1200 640">
  <path d="M185 2826 Q600 2892 1015 2826" fill="none" stroke="#2bbfb2" stroke-width="5"/>
  <g fill="#fff">
    <polygon points="45,3067 95,2958 255,2958 305,3067 255,3176 95,3176"/>
    <polygon points="325,3067 375,2958 535,2958 585,3067 535,3176 375,3176"/>
    <polygon points="604,3067 654,2958 814,2958 864,3067 814,3176 654,3176"/>
    <polygon points="882,3067 932,2958 1092,2958 1142,3067 1092,3176 932,3176"/>
  </g>
  <g fill="#27c3e6">
    <polygon points="268,2978 285,2978 320,3067 285,3156 268,3156 303,3067"/>
    <polygon points="548,2978 565,2978 600,3067 565,3156 548,3156 583,3067"/>
    <polygon points="827,2978 844,2978 879,3067 844,3156 827,3156 862,3067"/>
    <polygon points="1105,2978 1122,2978 1157,3067 1122,3156 1105,3156 1140,3067"/>
  </g>
  <path d="M0 3400 Q600 3300 1200 3400 L1200 3410 L0 3410 Z" fill="#fff"/>
  <path d="M120 3380 Q600 3310 1080 3380" fill="none" stroke="#2bbfb2" stroke-width="5"/>
</svg>
<div class="step-label" style="left:87px;top:2987px">Company</div>
<div class="step-art" style="left:100px;top:3035px;background:linear-gradient(135deg,#f6d25a,#f3b73c)" role="img" aria-label="Illustration of a light bulb made of puzzle pieces with small people"></div>
<div class="step-label" style="left:365px;top:2968px">Company<br>+<br>Venture Z</div>
<div class="step-art" style="left:380px;top:3040px;background:linear-gradient(135deg,#f6d25a,#2bbfb2)" role="img" aria-label="Illustration of the company puzzle bulb joined with a teal circle"></div>
<div class="step-label" style="left:644px;top:2968px">Design -<br>research - inventing<br>&amp; launch</div>
<div class="step-art" style="left:660px;top:3040px;background:linear-gradient(135deg,#f4c15a,#4b6fd8)" role="img" aria-label="Illustration of a person working at a desk with charts and a rocket"></div>
<div class="step-label" style="left:922px;top:2968px">Finalized<br>product &amp; happy<br>client</div>
<div class="step-art" style="left:937px;top:3040px;background:linear-gradient(135deg,#f3a046,#3d5bd0)" role="img" aria-label="Illustration of a happy client with a finished product on a screen"></div>
<a class="pill" style="left:536px;top:3216px;width:128px;height:34px">Get in Touch</a>

<!-- Services -->
<div class="services-title" style="top:3425px"><h2 class="h-main">Our Services</h2></div>
<div class="services-title" style="top:3472px"><h2 class="h-accent">We build teams that deliver!</h2></div>

<div class="card" style="left:88px">
  <div class="icon"></div><h3>Research</h3>
  <p>It is a long established fact that a reader will be distracted by the read-able content of a page.</p>
  <a class="btn-outline">Get in Touch</a>
</div>
<div class="card featured" style="left:344px">
  <div class="icon"></div><h3>Design</h3>
  <p>It is a long established fact that a reader will be distracted by the read-able content of a page.</p>
  <a class="btn-outline">Apply Here</a>
</div>
<div class="card" style="left:600px">
  <div class="icon"></div><h3>Engineers</h3>
  <p>It is a long established fact that a reader will be distracted by the read-able content of a page.</p>
  <a class="btn-outline">Our Approach</a>
</div>
<div class="col-divider"></div>
<div class="card" style="left:856px">
  <div class="icon"></div><h3>Product Managers</h3>
  <p>It is a long established fact that a reader will be distracted by the read-able content of a page.</p>
  <a class="btn-outline">Why Us</a>
</div>
<a class="btn-outline" style="left:520px;top:3895px;width:160px">View All Services</a>

<!-- Footer -->
<footer class="footer"></footer>
<svg class="abs" style="left:0;top:3960px" width="1200" height="140" viewBox="0 3960 1200 140">
  <path d="M0 3960 L1200 3960 L1200 3975 Q600 4110 0 3975 Z" fill="#fff"/>
  <path d="M280 4030 Q600 4080 920 4030" fill="none" stroke="#2bbfb2" stroke-width="5"/>
  <circle cx="600" cy="4051" r="40" fill="#2bbfb2" stroke="#fff" stroke-width="5"/>
</svg>
<div class="f-brand"><span class="brand-dot"></span>Venture Z</div>
<div class="f-call">Call. 800.555.0147</div>
<div class="f-mail">e. info@venturez.com</div>
<div class="social" style="left:88px"></div>
<div class="social active" style="left:137px"></div>
<div class="social" style="left:185px"></div>
<div class="f-head" style="left:506px;top:4172px">Quick links</div>
<ul class="quick">
  <li>Freelancers</li><li>Companies</li><li>Services</li><li>Our Approach</li><li>Why Us</li><li>FAQ</li><li>Contact Us</li>
</ul>
<div class="subscribe">
  <div class="f-head" style="left:24px;top:20px">Subscribe to our blog</div>
  <div class="field" style="top:82px">Your name</div>
  <div class="field" style="top:134px">name@email.com</div>
  <div class="submit">Submit</div>
</div>
<div class="legal" style="left:88px">© 2021 <span class="hl">Venture Z.</span> All Rights Reserved</div>
<div class="legal" style="left:505px">Privacy Policy</div>
<div class="legal" style="left:610px">Terms &amp; Conditions</div>
<div class="legal" style="left:751px">Security &amp; Compliance</div>

</body>
</html>
```